Business Card Design

www.tallowoodrise.com.au

Tallowood Rise Bed and Breakfast
A unique property with spectacular views situated in a peaceful quiet court surrounded by other quality homes. Set back from the street, this wonderful residence has plenty of space. The huge paved driveway has tonnes of off street parking

Relax in the beautifully landscaped lawn area with mature trees. The stunning balcony & deck is an ideal place to sit & watch the spectacular sunsets through the tree tops. Just wonderful!

The self-contained Bed and Breakfast has its own separate entrance door and consists of a large lounge/ kitchenette with sink & a separate bedroom. The bathroom has a glass shower screen, toilet & vanity unit.
If you are looking for your own piece of paradise in an ideal established setting with plenty of room then you must stay at Tallowood rise
This really is a slice of Heaven so come & stay!

- Established landscaped gardens & lawn areas
- paved driveway - loads of off street parking
- Splendid balcony with glorious views
- Close to shopping & transport

We welcome you to relax and unwind in the charm of our modern country feel bed and breakfast in the Northern Suburbs of Adelaide, offering privacy and relaxation, it is perfect for couples
This self-contained bed & breakfast will provide you with a “home away from home”, including breakfast provisions and all the comfort and modern conveniences you’d expect Tallowood Rise is perfect whether you’re on a holiday visit to Adelaide or here for business.
Enjoy the many activities Adelaide has to offer, we are positioned in the Northern Suburbs for you to easily travel to the Adelaide Hills or Barossa Wine region.
Tallowood Rise B & B is in a fantastic location for whatever you want to do on your visit to South Australia. Nestled within walking distance to the Marlow Creek or visit our world renowned wine regions. Of course, we can help and point you in the right direction.

Industry/Entity Type

Shopping

Contact Information for Business Card

14 Tallowood Court
Marlow Heights SA 5172

Doug & Fiona Prestley
0455 316 974 or 0438 625 407
www.tallowoodrise.com.au
doug@tallowoodrise.com.au

```html
<!DOCTYPE html>
<html lang="en">
<head>
<meta charset="utf-8">
<title>Tallowood Rise Bed &amp; Breakfast – Business Card</title>
<link rel="stylesheet" href="https://fonts.googleapis.com/css2?family=Amaranth:wght@700&family=Open+Sans:wght@600&display=swap">
<style>
  :root {
    --backdrop: #ece8df;
    --card-light: #f6e9b4;
    --card-dark: #e7d08f;
    --ink: #8b6e70;
    --bloom-soft: rgba(244, 211, 90, 0.35);
    --bloom-faint: rgba(244, 211, 90, 0.12);
    --stem: rgba(240, 205, 95, 0.7);
  }
  * { box-sizing: border-box; margin: 0; padding: 0; }
  html, body { width: 1200px; height: 1050px; overflow: hidden; }
  body {
    background: var(--backdrop);
    display: flex;
    flex-direction: column;
    align-items: center;
    justify-content: center;
    gap: 30px;
  }
  .card {
    position: relative;
    width: 840px;
    height: 480px;
    background: linear-gradient(135deg, var(--card-light) 0%, var(--card-light) 40%, var(--card-dark) 100%);
    box-shadow: 0 6px 18px rgba(0, 0, 0, 0.18);
    overflow: hidden;
    color: var(--ink);
  }
  .flower-art {
    position: absolute;
    border-radius: 40px;
    background: radial-gradient(ellipse at 50% 25%, var(--bloom-soft) 0%, var(--bloom-faint) 55%, transparent 80%);
  }
  .ring {
    position: absolute;
    width: 30px;
    height: 30px;
    border: 2px solid var(--stem);
    border-radius: 50%;
  }
  .brand { position: absolute; z-index: 1; }
  .brand-name, .brand-tagline {
    font-family: "Amaranth", sans-serif;
    font-weight: 700;
    line-height: 1;
    white-space: nowrap;
  }
  .text {
    font-family: "Open Sans", sans-serif;
    font-weight: 600;
    position: absolute;
    z-index: 1;
    white-space: nowrap;
  }

  /* Front */
  .front .brand { left: 170px; top: 180px; }
  .front .brand-name { font-size: 72px; }
  .front .brand-tagline { font-size: 34px; margin-left: 160px; margin-top: 6px; }
  .front .art-left { left: 30px; top: 30px; width: 150px; height: 380px; }
  .front .art-mid { left: 300px; top: 10px; width: 200px; height: 160px; }
  .front .art-right { left: 600px; top: 290px; width: 210px; height: 170px; }
  .front .ring-a { left: 58px; top: 128px; }
  .front .ring-b { left: 340px; top: 390px; }

  /* Back */
  .back .brand { left: 70px; top: 55px; }
  .back .brand-name { font-size: 52px; }
  .back .brand-tagline { font-size: 22px; margin-top: 6px; }
  .back .art-left { left: 30px; top: 170px; width: 170px; height: 130px; }
  .back .art-mid { left: 210px; top: 140px; width: 140px; height: 150px; }
  .back .ring-a { left: 370px; top: 330px; }
  .back .ring-b { left: 560px; top: 405px; }
  .back .address {
    left: 70px; top: 320px;
    font-size: 19px; line-height: 1.45;
    font-style: normal;
  }
  .back .person { left: 420px; top: 200px; }
  .back .person-name { font-size: 31px; }
  .back .phones { font-size: 19px; margin-top: 40px; }
  .back .email { font-size: 19px; margin-top: 24px; }
</style>
</head>
<body>
  <section class="card front" aria-label="Business card front">
    <div class="flower-art art-left" role="img" aria-label="Stylised yellow wildflower sprig"></div>
    <div class="flower-art art-mid" role="img" aria-label="Stylised yellow wildflower sprig"></div>
    <div class="flower-art art-right" role="img" aria-label="Stylised yellow wildflower sprig"></div>
    <span class="ring ring-a"></span>
    <span class="ring ring-b"></span>
    <div class="brand">
      <div class="brand-name">Tallowood Rise</div>
      <div class="brand-tagline">Bed &amp; Breakfast</div>
    </div>
  </section>

  <section class="card back" aria-label="Business card back">
    <div class="flower-art art-left" role="img" aria-label="Stylised yellow wildflower sprig"></div>
    <div class="flower-art art-mid" role="img" aria-label="Stylised yellow wildflower sprig"></div>
    <span class="ring ring-a"></span>
    <span class="ring ring-b"></span>
    <div class="brand">
      <div class="brand-name">Tallowood Rise</div>
      <div class="brand-tagline">Bed &amp; Breakfast</div>
    </div>
    <address class="address text">
      14 Tallowood Court<br>
      Marlow Heights<br>
      SA 5172<br>
      www.tallowoodrise.com.au
    </address>
    <div class="person text">
      <div class="person-name">Doug &amp; Fiona Prestley</div>
      <div class="phones">0455 316 974, 0438 625 407</div>
      <div class="email">doug@tallowoodrise.com.au</div>
    </div>
  </section>
</body>
</html>
```